Become an EMT and Serve your community!

We are looking to design a postcard that will be mailed to surrounding communities that notifies them of our upcoming EMT class with an emphasis of serving their community. We are looking for a design that grabs peoples attention and motivates them to sign up and serve their community. Our primary colors are red and blue. We would like to incorporate the Institute logo as well as one or two photos. We do have more photos available upon request. Our Institute website is www.halvorsenacademy.net for more material. It is important that the postcard meets mailing guidelines.

Target Market(s)

Local community members

Industry/Entity Type

Education

Font styles to use
Sans Serif

Colors
f04a50
3176b5
0255a3
eaf1f7

Requirements
Must have
• Dates
Prices
Contact info
Look interesting
Convey the message of “Serving your Community”
Nice to have
• Clear information
Concise
Incorporate an action shot
Should not have
• Generic EMS logos

```html
<!DOCTYPE html>
<html lang="en">
<head>
<meta charset="utf-8">
<title>2020 Summer EMT Class Postcard</title>
<link href="https://fonts.googleapis.com/css2?family=Montserrat:wght@600;800;900&family=Open+Sans:wght@400;600;700&display=swap" rel="stylesheet">
<style>
  :root{
    --red:#f04a50;
    --blue:#3176b5;
    --navy:#0255a3;
    --ice:#eaf1f7;
    --ink:#1f2d44;
    --photo-a:#3a3f4a;
    --photo-b:#7a5a4c;
    --bg:#e9e9e9;
    --white:#ffffff;
  }
  *{box-sizing:border-box;margin:0;padding:0}
  html,body{width:690px;height:1200px;overflow:hidden;background:var(--bg)}
  body{position:relative;font-family:"Open Sans",Arial,sans-serif;color:var(--ink)}
  .card{position:absolute;left:25px;width:640px;height:427px;background:var(--white);overflow:hidden;box-shadow:0 4px 14px rgba(0,0,0,.18)}
  .card--front{top:150px}
  .card--back{top:620px}
  .deco{position:absolute;inset:0}
  .photo{position:absolute;background:linear-gradient(135deg,var(--photo-a),var(--photo-b) 60%,var(--photo-a))}
  .brand-mark{position:absolute;border-radius:50%;background:var(--navy);border:4px solid var(--white);box-shadow:0 0 0 2px var(--blue)}
  .badge{position:absolute;width:46px;height:46px;border-radius:50%;background:var(--red);border:3px solid var(--white)}
  .brand-name{position:absolute;font-family:"Montserrat",Arial,sans-serif;font-weight:800;color:var(--navy);font-size:10px;line-height:1.15;text-transform:uppercase}

  /* front */
  .front-photo{left:0;top:44px;width:312px;height:250px;border-radius:0 0 160px 0}
  .front-photo-round{left:48px;top:236px;width:122px;height:122px;border-radius:50%;border:5px solid var(--white);box-shadow:0 0 0 3px var(--red)}
  .front-badge{left:18px;top:300px}
  .front-mark{left:322px;top:28px;width:66px;height:66px}
  .title{position:absolute;left:398px;top:28px;font-family:"Montserrat",Arial,sans-serif;font-weight:900;color:var(--navy);font-size:24px;line-height:1.05;text-transform:uppercase}
  .tagline{position:absolute;left:392px;top:82px;width:248px;height:22px;background:var(--red);color:var(--white);font-family:"Montserrat",Arial,sans-serif;font-weight:800;font-size:11px;line-height:22px;padding-left:18px;letter-spacing:.5px;text-transform:uppercase}
  .when{position:absolute;left:330px;top:124px;width:290px}
  .when h2{font-family:"Montserrat",Arial,sans-serif;font-weight:900;color:var(--navy);font-size:22px;text-align:center;letter-spacing:1px;margin-bottom:6px}
  .when p{font-size:10.5px;line-height:1.4;margin-bottom:8px}
  .when strong{color:var(--navy)}
  .when .accent{color:var(--red);font-weight:700}
  .contact{position:absolute;display:flex;align-items:center;gap:14px;font-family:"Montserrat",Arial,sans-serif;font-weight:800;font-size:12px;color:var(--navy)}
  .contact span{display:flex;align-items:center;gap:6px}
  .contact .web{font-size:10px;color:var(--blue)}
  .front-contact{left:330px;top:352px}
  .icon{width:18px;height:18px;flex:none}

  /* back */
  .tuition-tab{position:absolute;left:0;top:22px;width:150px;height:34px;background:var(--red);border-radius:0 17px 17px 0;color:var(--white);font-family:"Montserrat",Arial,sans-serif;font-weight:900;font-size:18px;line-height:34px;padding-left:24px;letter-spacing:1px}
  .prices{position:absolute;left:24px;top:68px;width:290px;font-family:"Montserrat",Arial,sans-serif}
  .prices .price{color:var(--red);font-weight:800;font-size:15px}
  .prices .price small{font-family:"Open Sans",Arial,sans-serif;font-weight:600;font-size:10px;color:var(--ink)}
  .prices .deposit{color:var(--navy);font-weight:800;font-size:15px;line-height:1.2;margin-top:6px}
  .pitch{position:absolute;left:0;top:150px;width:326px;height:92px;background:var(--navy);color:var(--white);font-size:10px;line-height:1.45;padding:10px 18px 10px 24px}
  .back-photo{left:0;top:250px;width:326px;height:177px;border-radius:0 120px 0 0}
  .divider{position:absolute;left:344px;top:30px;width:1px;height:330px;background:#c9d3de}
  .back-mark{left:366px;top:24px;width:52px;height:52px}
  .back-badge{left:428px;top:27px}
  .back-name{left:366px;top:84px;width:130px}
  .stamp{position:absolute;right:22px;top:22px;width:62px;height:74px;border:1.5px dashed #9aa7b6}
  .address-lines{position:absolute;left:384px;top:210px;width:230px}
  .address-lines i{display:block;height:1px;background:#b8c3cf;margin-bottom:26px}
  .return{position:absolute;left:366px;top:330px;font-size:9.5px;line-height:1.4;color:var(--ink)}
  .return strong{color:var(--navy);font-family:"Montserrat",Arial,sans-serif}
  .back-contact{left:366px;top:386px}
  .band{position:absolute;left:0;right:0;bottom:0;height:14px;background:var(--navy)}
</style>
</head>
<body>

<section class="card card--front" aria-label="Postcard front">
  <svg class="deco" viewBox="0 0 640 427" aria-hidden="true">
    <rect x="0" y="0" width="640" height="427" fill="var(--white)"/>
    <path d="M0 0 H330 C320 30 300 40 300 44 H0 Z" fill="var(--red)"/>
    <path d="M392 0 H640 V20 H400 Z" fill="var(--ice)"/>
    <path d="M0 400 H640 V427 H0 Z" fill="var(--navy)"/>
    <path d="M0 392 H640 V400 H0 Z" fill="var(--red)"/>
  </svg>
  <div class="photo front-photo" role="img" aria-label="Action photo of EMT students practicing CPR on a training manikin"></div>
  <div class="photo front-photo-round" role="img" aria-label="Photo of EMT students treating a patient in class"></div>
  <div class="badge front-badge" aria-hidden="true"></div>

  <div class="brand-mark front-mark" aria-hidden="true"></div>
  <h1 class="title">2020 Summer<br>EMT Class</h1>
  <div class="tagline">Serving your community</div>

  <div class="when">
    <h2>WHEN</h2>
    <p><strong>Monday, Tuesday, Wednesday</strong> from <span class="accent">May 26th</span> through <span class="accent">August 17th</span>.</p>
    <p><span class="accent">Wednesdays:</span> Students will need to sign up for either a <strong>4:00p-7:00p</strong> lab session, or a <strong>7:00p-10:00p</strong> lab session.</p>
    <p>There will be one required <strong>Sat/Sun</strong> weekend field for all students. This will take place on <span class="accent">June 13th &amp; 14th</span>. <strong>Weekend classes</strong> will run from <span class="accent">8:00am - 8:00pm</span>.</p>
  </div>

  <div class="contact front-contact">
    <span>
      <svg class="icon" viewBox="0 0 24 24"><circle cx="12" cy="12" r="12" fill="var(--red)"/><path d="M8.5 6.5l2 2.5-1.2 1.4c.8 1.7 2 2.9 3.6 3.7l1.4-1.2 2.5 2-1.3 2c-4.6-.6-8.3-4.3-8.8-8.9z" fill="var(--white)"/></svg>
      555-214-0387
    </span>
    <span class="web">
      <svg class="icon" viewBox="0 0 24 24"><circle cx="12" cy="12" r="12" fill="var(--blue)"/><circle cx="12" cy="12" r="6" fill="none" stroke="var(--white)" stroke-width="1.5"/><path d="M6 12h12M12 6c-2.5 3-2.5 9 0 12M12 6c2.5 3 2.5 9 0 12" fill="none" stroke="var(--white)" stroke-width="1.2"/></svg>
      www.halvorsenacademy.net
    </span>
  </div>
</section>

<section class="card card--back" aria-label="Postcard back">
  <div class="tuition-tab">TUITION</div>
  <div class="prices">
    <div class="price">$1000 EMT <small>(without CPR).</small></div>
    <div class="deposit">$250 deposit is due<br>at time of registration.</div>
  </div>
  <p class="pitch">Serve your community and become an Emergency Medical Technician. As a student you will have access to cutting edge training equipment, experienced instructors, and be able to train on a 911 Ambulance through Halvorsen EMS!</p>
  <div class="photo back-photo" role="img" aria-label="Action photo of EMTs loading a patient into an ambulance at night"></div>

  <div class="divider" aria-hidden="true"></div>
  <div class="brand-mark back-mark" aria-hidden="true"></div>
  <div class="badge back-badge" aria-hidden="true"></div>
  <div class="brand-name back-name">Halvorsen Academy</div>
  <div class="stamp" aria-hidden="true"></div>

  <div class="address-lines" aria-hidden="true"><i></i><i></i><i></i></div>

  <p class="return"><strong>Halvorsen Academy of EMS</strong><br>18 Linden Road, Harlow, NH 03800</p>

  <div class="contact back-contact">
    <span>
      <svg class="icon" viewBox="0 0 24 24"><circle cx="12" cy="12" r="12" fill="var(--red)"/><path d="M8.5 6.5l2 2.5-1.2 1.4c.8 1.7 2 2.9 3.6 3.7l1.4-1.2 2.5 2-1.3 2c-4.6-.6-8.3-4.3-8.8-8.9z" fill="var(--white)"/></svg>
      555-214-0387
    </span>
    <span class="web">www.halvorsenacademy.net</span>
  </div>
  <div class="band" aria-hidden="true"></div>
</section>

</body>
</html>
```